RISE with Abbot Leng Book Cover

We need a Book cover for a Spiritual Book entitled:

R.I.S.E. with Abbot Leng: Reflective Inner Study Exercises with a Present Era Hermit Sage

By Ven. Abbot Leng Odile Rask, MPH

By 2x No. 1 Best Selling Author

See sketch: By 2x No. 1 Best Selling Author in WHITE Text
The tape where above is written and 1 in red Text

ABBOT LENG ODILE RASK, MPH (White and Thick BOLD TEXT - see attachment KE Baltor)

R.I.S.E. ABBOT LENG (Use the Wayfinder FONT and style in WHITE text/colour)

with (use the Corinne Haldwell book - No. 1 Best Seller Text Style in white or red)

Reflective Inner Study Exercises with a Present Era Hermit Sage (Use Harwick book - red block at the bottom)

Please clean up the picture as it is a raw file and take out the shadow on Abbot Leng's face. Make us more translucent and light filled. Clean up the face and crop to look like the sketch (cro just underneath the white cuff on Monk's sleeve). Keep to of pic as it to use the right hand space for By No. 1 Best Selling Author and No. 1 text and red band.

```html
<!DOCTYPE html>
<html lang="en">
<head>
<meta charset="utf-8">
<title>R.I.S.E. with Abbot Leng — Book Cover</title>
<link rel="stylesheet" href="https://fonts.googleapis.com/css2?family=Roboto+Condensed:wght@700;800&display=swap">
<style>
  :root {
    --stage-bg: #c4e6f8;
    --cover-dark: #0b0b0b;
    --photo-top: #6d6a45;
    --photo-mid: #3a3a2c;
    --brand-red: #e31b23;
    --ink-white: #ffffff;
    --ink-black: #000000;
  }
  * { margin: 0; padding: 0; box-sizing: border-box; }
  html, body {
    width: 1200px;
    height: 1000px;
    overflow: hidden;
    background: var(--stage-bg);
    font-family: "Roboto Condensed", "Arial Narrow", sans-serif;
  }
  .book-cover {
    position: absolute;
    left: 289px;
    top: 30px;
    width: 612px;
    height: 792px;
    overflow: hidden;
    background: var(--cover-dark);
  }
  .cover-photo {
    position: absolute;
    inset: 0;
    background:
      radial-gradient(ellipse at 30% 35%, rgba(200,170,140,0.35), transparent 45%),
      radial-gradient(ellipse at 72% 30%, rgba(210,170,140,0.35), transparent 40%),
      linear-gradient(180deg, var(--photo-top) 0%, var(--photo-mid) 35%, #161614 62%, var(--cover-dark) 80%);
  }
  .author-name {
    position: absolute;
    top: 44px;
    color: var(--ink-white);
    font-weight: 800;
    font-size: 23px;
    letter-spacing: 0.2px;
    line-height: 1;
  }
  .author-name--first { left: 26px; }
  .author-name--second { left: 246px; }
  .cover-graphics {
    position: absolute;
    inset: 0;
    width: 612px;
    height: 792px;
  }
  .subtitle-block {
    position: absolute;
    left: 31px;
    top: 656px;
    width: 538px;
    height: 117px;
    background: var(--brand-red);
    display: flex;
    align-items: center;
    justify-content: center;
    text-align: center;
    color: var(--ink-white);
    font-weight: 700;
    font-size: 32px;
    line-height: 42px;
  }
</style>
</head>
<body>
  <main class="book-cover">
    <div class="cover-photo" role="img" aria-label="Photograph of the two authors in dark robes smiling at each other outdoors against soft green foliage"></div>

    <p class="author-name author-name--first">ABBOT LENG</p>
    <p class="author-name author-name--second">ODILE RASK, MPH</p>

    <svg class="cover-graphics" viewBox="0 0 612 792" xmlns="http://www.w3.org/2000/svg">
      <g class="bestseller-ribbon">
        <polygon points="388,0 432,0 612,132 612,178" fill="var(--brand-red)"/>
        <text x="0" y="0" transform="translate(500,82) rotate(36.5)" text-anchor="middle"
              fill="var(--ink-white)" font-family="Roboto Condensed, sans-serif" font-weight="800" font-size="14">BY 2X NO. 1 BEST SELLING AUTHOR</text>
      </g>
      <text class="rank-mark" x="551" y="68" text-anchor="middle" fill="var(--brand-red)" stroke="var(--ink-white)" stroke-width="2" paint-order="stroke"
            font-family="Roboto Condensed, sans-serif" font-weight="800" font-size="56">#1</text>

      <text class="title-main" x="31" y="525" textLength="542" lengthAdjust="spacingAndGlyphs"
            fill="var(--ink-white)" font-family="Roboto Condensed, sans-serif" font-weight="800" font-size="330">R.I.S.E.</text>

      <line class="title-rule" x1="31" y1="530" x2="573" y2="530" stroke="var(--ink-white)" stroke-width="3"/>
      <g class="title-with">
        <rect x="254" y="513" width="74" height="34" rx="17" fill="var(--ink-black)" stroke="var(--ink-white)" stroke-width="2"/>
        <text x="291" y="538" text-anchor="middle" fill="var(--ink-white)" font-family="Roboto Condensed, sans-serif" font-weight="700" font-size="24">with</text>
      </g>

      <text class="title-name" x="31" y="642" textLength="542" lengthAdjust="spacingAndGlyphs"
            fill="var(--ink-white)" font-family="Roboto Condensed, sans-serif" font-weight="800" font-size="126">ABBOT LENG</text>
    </svg>

    <h2 class="subtitle-block">Reflective Inner Study Exercises with<br>a Present Era Hermit Sage</h2>
  </main>
</body>
</html>
```